Bright Reed Acupuncture Studio Website Design

We are working with Bright Reed Acunpuncture Studio. They are a local Chinese medicine and acupuncture studio and in need of a new website design.

Some sites to use for inspiration:

https://marblecoveacupuncture.example
https://steadfernacupuncture.example
https://quietharborclinic.example
https://emberdawnacupuncture.example
https://cedarbrookclinic.example

Thank you for taking the time to consider designing a website for us. We are web developers based in Stockton, CA, USA. Most of our projects go through the same process. Understanding this process may help you win a project with us. We custom-code all of our websites in-house. We don’t have any requirements as to what tools you use for your design, but we prefer Figma files. For any design that we label as four-stars, we send it to the client for review. The client picks the final design they want us to use. Once we complete this process, we will continue to show additional clients all the four-star sites and purchase them later. Your designs will have multiple chances to sell. For better chances of success, we ask that you follow these guidelines.

IMAGES:
If you use any images or icons in the design, we ask that you have a link to the asset so we can purchase the image/icon. Most of the designs we submit do not have the customer’s images on them unless they have some great images. Be creative; show us the feeling you are trying to portray with your image choices. Use any royalty-free site you choose. We subscribe to Adobe and mainly use their images, but we can purchase images outside of Adobe.

PLEASE NOTE: we will not submit designs to clients with watermarks on the images.

FONTS:
We ask that you identify the fonts used in the design. This can be done in a message if you want. We typically use Google Fonts and Adobe Fonts.

CONTENT:
We're always open to different content and ideas. We often submit designs with stock images so the client can see our vision. We typically take pictures after the website launch to use their images with our vision. Lorem Ipsum is fine for paragraphs, but we ask that you write the headers in correct English. We want to be able to show the vision and identify the sections of the website.

INSPIRATION:
We typically add a couple of links in the brief of websites we like to help you get started in your design.

REVISIONS:
We do not often ask for revisions of the designs unless we see something in the design that may not appeal to the client. If there are slight changes that we want to make, we do that in the development process.

FEEDBACK:
We rarely give feedback on designs during the design process. We are working on many website projects and do not have the time to provide feedback. We usually respond if your request is well thought out and asks specific questions, but a note asking “feedback, please” usually goes unanswered.

```html
<!DOCTYPE html>
<html lang="en">
<head>
<meta charset="utf-8">
<title>Bright Reed Acupuncture Studio</title>
<link href="https://fonts.googleapis.com/css2?family=Poppins:ital,wght@0,300;0,400;0,500;0,600;0,700;1,400&display=swap" rel="stylesheet">
<style>
:root{
  --coral:#e0625a;
  --navy:#1f2a37;
  --ink:#222428;
  --text:#4a4d52;
  --mist:#f5f5f5;
  --blush:#fdeeee;
  --white:#ffffff;
}
*{margin:0;padding:0;box-sizing:border-box}
html,body{width:1200px;height:5208px;overflow:hidden}
body{font-family:'Poppins',sans-serif;color:var(--ink);background:var(--white);position:relative}
.abs{position:absolute}
.brand{font-family:'Poppins',sans-serif;font-weight:600;color:var(--navy);display:flex;align-items:center;gap:12px}
.brand-dot{width:28px;height:28px;border-radius:50%;background:var(--coral)}
.nav a{position:absolute;top:58px;font-size:13px;color:var(--ink);text-decoration:none}
.nav a.active{color:var(--coral)}
.nav a.active::after{content:"";position:absolute;left:0;right:0;bottom:-10px;height:2px;background:var(--coral)}
.pill{position:absolute;border-radius:40px;display:flex;align-items:center;justify-content:center;gap:14px;font-size:15px;font-weight:600;color:var(--white);text-transform:uppercase}
.pill .ar{width:20px;height:20px;border-radius:50%;background:rgba(255,255,255,.25);display:flex;align-items:center;justify-content:center}
.dark{background:var(--navy)}
.coralbg{background:var(--coral)}
.circ{position:absolute;width:52px;height:52px;border-radius:50%;display:flex;align-items:center;justify-content:center}
.circ.outline{border:2px solid var(--ink);background:var(--white)}
.circ.fill{background:var(--coral)}
.photo{position:absolute}
.sec-mark{position:absolute;left:578px;width:44px;height:44px;border-radius:50%;border:3px solid var(--navy)}
.sec-title{position:absolute;left:0;width:1200px;text-align:center;font-size:48px;font-weight:500;color:var(--ink);line-height:1.2}
.card{position:absolute;width:296px;height:246px;border-radius:14px;overflow:hidden}
.card span{position:absolute;left:0;right:0;bottom:24px;text-align:center;color:var(--white);font-size:23px;font-weight:600;line-height:1.2}
.benefits{position:absolute;left:196px;top:3094px;list-style:none}
.benefits li{display:flex;align-items:center;gap:20px;height:42px;font-size:14px;color:var(--ink)}
.benefits li i{width:16px;height:16px;border-radius:50%;background:var(--coral);display:flex;align-items:center;justify-content:center}
.quote{position:absolute;top:3878px;width:342px;height:147px;background:var(--blush);border-radius:6px}
.quote p{position:absolute;left:26px;right:26px;top:38px;font-size:13px;font-style:italic;line-height:25px;text-align:justify;text-align-last:center;color:var(--ink)}
.qmark{position:absolute;left:28px;top:-16px;font-size:90px;font-weight:700;color:var(--coral);line-height:1;font-family:'Poppins',sans-serif}
.person{position:absolute;top:4050px;display:flex;align-items:center;gap:18px}
.avatar{width:58px;height:58px;border-radius:50%;background:linear-gradient(135deg,#c9b3a3,#6f5f58)}
.person b{display:block;font-size:19px;font-weight:500;color:var(--ink);line-height:1.1}
.person small{display:block;font-size:11px;color:var(--text)}
.stars{color:#f4b400;font-size:11px;letter-spacing:1px}
.footer{position:absolute;left:0;top:4808px;width:1200px;height:400px;background:var(--navy);color:var(--white)}
.footer h4{position:absolute;top:92px;font-size:17px;font-weight:600}
.footer h4::after{content:"";position:absolute;left:0;bottom:-10px;width:64px;height:2px;background:var(--coral)}
.flinks{position:absolute;left:560px;top:152px;list-style:none}
.flinks li{height:27px;font-size:13px;display:flex;align-items:center;gap:14px}
.flinks li::before{content:"";width:9px;height:9px;border-radius:50%;background:var(--coral)}
.contact{position:absolute;left:808px;display:flex;gap:18px;align-items:center;font-size:13px;line-height:17px}
.contact .ic{width:34px;height:34px;border-radius:50%;background:var(--coral);display:flex;align-items:center;justify-content:center;flex:none}
.social{position:absolute;top:348px;width:24px;height:24px;border-radius:50%;background:var(--coral)}
</style>
</head>
<body>

<!-- Header -->
<header>
  <div class="brand abs" style="left:66px;top:36px;font-size:38px">
    <span class="brand-dot"></span>Bright Reed
  </div>
  <nav class="nav">
    <a href="#" class="active" style="left:418px">HOME</a>
    <a href="#" style="left:494px">ABOUT US</a>
    <a href="#" style="left:590px">SERVICES</a>
    <a href="#" style="left:684px">BLOG</a>
    <a href="#" style="left:750px">CONTACT US</a>
  </nav>
  <div class="pill dark" style="left:858px;top:42px;width:276px;height:44px;font-size:13px">Schedule Your Consultation</div>
</header>

<!-- Hero -->
<section class="hero">
  <div class="abs" style="left:0;top:122px;width:1200px;height:686px;background:var(--mist)"></div>
  <div class="abs" style="left:110px;top:228px;font-size:32px;font-weight:600;color:var(--navy);display:flex;align-items:center;gap:8px">Bright Reed
    <svg width="70" height="10"><circle cx="5" cy="5" r="4" fill="#e0625a"/><line x1="10" y1="5" x2="70" y2="5" stroke="#e0625a" stroke-width="2"/></svg>
  </div>
  <h1 class="abs" style="left:110px;top:274px;font-size:45px;line-height:54px;font-weight:400;color:var(--coral)">
    Experience the<br>Transformative Power<br>of <span style="color:var(--ink);font-weight:500">Chinese Medicine &amp;</span><br><span style="color:var(--ink);font-weight:500">Acupuncture Studio</span>
  </h1>
  <div class="pill coralbg" style="left:110px;top:520px;width:220px;height:60px">Our Services <span class="ar">›</span></div>
  <div class="pill dark" style="left:110px;top:602px;width:320px;height:60px">Schedule Appointment <span class="ar">›</span></div>
  <div class="circ outline" style="left:510px;top:714px"><svg width="14" height="14" viewBox="0 0 14 14"><path d="M9 2L4 7l5 5" stroke="#222" stroke-width="2.5" fill="none"/></svg></div>
  <div class="circ fill" style="left:570px;top:714px"><svg width="14" height="14" viewBox="0 0 14 14"><path d="M5 2l5 5-5 5" stroke="#fff" stroke-width="2.5" fill="none"/></svg></div>
  <div class="photo" style="left:656px;top:176px;width:478px;height:702px;border-radius:239px 239px 0 0;background:var(--coral)"></div>
  <div class="photo" role="img" aria-label="Therapist giving a relaxing treatment to a woman lying on a massage table" style="left:656px;top:196px;width:478px;height:682px;border-radius:239px 239px 0 0;background:linear-gradient(180deg,#ecebea,#d8d5d2 60%,#f3f2f0)"></div>
</section>

<!-- About -->
<section class="about">
  <div class="sec-mark" style="top:986px"></div>
  <h2 class="sec-title" style="top:1050px">Integrating Chinese Medicine<br>and Acupuncture Studio</h2>
  <div class="abs" style="left:76px;top:1232px;width:530px;height:456px;border-radius:110px 0 0 0;background:var(--coral)"></div>
  <div class="photo" role="img" aria-label="Practitioner in a silk robe massaging a client's back" style="left:0;top:1244px;width:614px;height:444px;border-radius:100px 0 0 0;background:linear-gradient(135deg,#e6e9ea,#6fa7a6 45%,#2f3d55)"></div>
  <h3 class="abs" style="left:674px;top:1282px;font-size:31px;font-weight:500;color:var(--coral)">Bright Reed Acupuncture Studio</h3>
  <p class="abs" style="left:674px;top:1336px;width:442px;font-size:14.5px;line-height:26.5px;color:var(--text);text-align:justify">Lorem ipsum dolor sit amet, consectetur adipiscing elit, sed do eius mod tempor incididunt ut labore et dolore magna aliqua. Ut enim ad minim veniam, quis nostrud exercitation ullamco laboris nisi ut aliquip ex ea commodo consequat. Duis aute irure dolor in repre henderit in voluptate velit esse cillum dolore eu fugiat nulla pariatur. Excepteur sint occaecat cupidatat non proident, sunt in culpa qui officia deserunt mollit anim id est laborum.</p>
  <div class="pill dark" style="left:674px;top:1582px;width:184px;height:48px;font-size:14px">Read More <span class="ar">›</span></div>
</section>

<!-- Services -->
<section class="services">
  <div class="sec-mark" style="top:1810px"></div>
  <h2 class="sec-title" style="top:1872px">Our Services</h2>
  <div class="abs" style="left:355px;top:2017px;width:490px;height:490px;border-radius:50%;background:#f3f3f3"></div>
  <div class="abs" style="left:405px;top:2067px;width:390px;height:390px;border-radius:50%;background:var(--white);box-shadow:0 6px 24px rgba(0,0,0,.12);display:flex;align-items:center;justify-content:center;gap:12px;font-size:34px;font-weight:600;color:var(--navy)"><span class="brand-dot"></span>Bright Reed</div>
  <div class="card" role="img" aria-label="Microneedling facial treatment" style="left:68px;top:2018px;background:linear-gradient(160deg,#e9e9e9,#8c8c8c)"><span>Microneedling</span></div>
  <div class="card" role="img" aria-label="Acupuncture needles in a client's back" style="left:836px;top:2018px;background:linear-gradient(160deg,#e3c0a6,#7a5540)"><span>Acupuncture</span></div>
  <div class="card" role="img" aria-label="Chinese bodywork session by candlelight" style="left:68px;top:2336px;background:linear-gradient(160deg,#d9b894,#5f7e80 60%,#3b2e2a)"><span>Chinese Bodywork</span></div>
  <div class="card" role="img" aria-label="Fire cupping glass cups on a back" style="left:838px;top:2336px;background:linear-gradient(160deg,#eeeeee,#8e8a86)"><span>Fire Cupping</span></div>
  <div class="card" role="img" aria-label="Acupoint injection into the skin" style="left:452px;top:2535px;background:linear-gradient(160deg,#e7c3a6,#9b7a66)"><span>Acupoint Injection<br>Therapy</span></div>
</section>

<!-- How it works -->
<section class="works">
  <div class="sec-mark" style="top:2892px"></div>
  <h2 class="sec-title" style="top:2956px">How Acupuncture Works!</h2>
  <ul class="benefits">
    <li><i></i>Painfree living</li>
    <li><i></i>Enhanced Digestion &amp; Immune Function</li>
    <li><i></i>Balanced Hormones</li>
    <li><i></i>Improved Mental Wellbeing</li>
    <li><i></i>Radiant Glowing Skin</li>
    <li><i></i>Restored Sleep &amp; Energy Levels</li>
    <li><i></i>Balanced Stress Levels</li>
    <li><i></i>Painfree &amp; Regulated Periods</li>
    <li><i></i>Optimized Fertility</li>
    <li><i></i>Pregnancy Support</li>
    <li><i></i>Menopause Support</li>
  </ul>
  <div class="abs" style="left:568px;top:3086px;width:446px;height:496px;background:var(--coral)"></div>
  <div class="photo" role="img" aria-label="Facial acupuncture treatment on a relaxed client" style="left:560px;top:3100px;width:442px;height:492px;background:linear-gradient(160deg,#2b3a55,#d8c4b6 55%,#f1efec)"></div>
</section>

<!-- Testimonials -->
<section class="testimonials">
  <div class="sec-mark" style="top:3684px"></div>
  <h2 class="sec-title" style="top:3748px">What Our Client Says About Us</h2>
  <div class="quote" style="left:68px"><div class="qmark">“</div><p>Lorem ipsum dolor sit amet, conse ctetuer adipiscing elit. Aenean comodo ligula eget dolor. Aenean massa. Cum sociis natoque pen atibus et magnis</p></div>
  <div class="quote" style="left:429px"><div class="qmark">“</div><p>Lorem ipsum dolor sit amet, conse ctetuer adipiscing elit. Aenean comodo ligula eget dolor. Aenean massa. Cum sociis natoque pen atibus et magnis</p></div>
  <div class="quote" style="left:790px"><div class="qmark">“</div><p>Lorem ipsum dolor sit amet, conse ctetuer adipiscing elit. Aenean comodo ligula eget dolor. Aenean massa. Cum sociis natoque pen atibus et magnis</p></div>
  <div class="person" style="left:132px"><div class="avatar" role="img" aria-label="Client portrait"></div><div><b>Marcus Hale</b><small>Managing Director</small><div class="stars">★★★★★</div></div></div>
  <div class="person" style="left:493px"><div class="avatar" role="img" aria-label="Client portrait"></div><div><b>Owen Pratt</b><small>Managing Director</small><div class="stars">★★★★★</div></div></div>
  <div class="person" style="left:854px"><div class="avatar" role="img" aria-label="Client portrait"></div><div><b>Leo Carver</b><small>Managing Director</small><div class="stars">★★★★★</div></div></div>
  <div class="circ outline" style="left:543px;top:4174px"><svg width="14" height="14" viewBox="0 0 14 14"><path d="M9 2L4 7l5 5" stroke="#222" stroke-width="2.5" fill="none"/></svg></div>
  <div class="circ fill" style="left:603px;top:4174px"><svg width="14" height="14" viewBox="0 0 14 14"><path d="M5 2l5 5-5 5" stroke="#fff" stroke-width="2.5" fill="none"/></svg></div>
</section>

<!-- Newsletter -->
<section class="newsletter">
  <div class="abs" style="left:0;top:4332px;width:1200px;height:476px;background:var(--blush)"></div>
  <div class="sec-mark" style="top:4410px"></div>
  <h2 class="sec-title" style="top:4474px">Stay Balanced &amp; Informed</h2>
  <p class="abs" style="left:0;top:4562px;width:1200px;text-align:center;font-size:22px;color:var(--ink)">Sign Up Now for Our Newsletter</p>
  <div class="abs" style="left:284px;top:4632px;width:632px;height:94px;background:var(--white);border-radius:10px;box-shadow:0 2px 8px rgba(0,0,0,.08)"></div>
  <span class="abs" style="left:312px;top:4667px;font-size:16px;color:#8a8d92">Enter Email Address</span>
  <div class="abs" style="left:766px;top:4632px;width:150px;height:94px;background:var(--navy);border-radius:0 10px 10px 0;color:var(--white);font-size:21px;font-weight:600;display:flex;align-items:center;justify-content:center">SIGNUP</div>
</section>

<!-- Footer -->
<footer class="footer">
  <div class="brand abs" style="left:108px;top:132px;font-size:48px;color:var(--white)"><span class="brand-dot" style="width:36px;height:36px"></span>Bright Reed</div>
  <h4 style="left:560px">QUICK LINKS</h4>
  <ul class="flinks"><li>About Us</li><li>Services</li><li>Blog</li><li>Contact Us</li></ul>
  <h4 style="left:808px">CONTACT US</h4>
  <div class="contact" style="top:150px"><span class="ic"><svg width="16" height="16" viewBox="0 0 24 24"><path d="M6.6 10.8a15 15 0 006.6 6.6l2.2-2.2c.3-.3.7-.4 1-.2 1.1.4 2.3.6 3.6.6.6 0 1 .4 1 1V20c0 .6-.4 1-1 1A17 17 0 013 4c0-.6.4-1 1-1h3.5c.6 0 1 .4 1 1 0 1.3.2 2.5.6 3.6.1.3 0 .7-.2 1z" fill="#fff"/></svg></span><div>CALL US<br>012 555 0148</div></div>
  <div class="contact" style="top:206px"><span class="ic"><svg width="16" height="16" viewBox="0 0 24 24"><rect x="3" y="6" width="18" height="13" rx="2" fill="#fff"/><path d="M3 7l9 6 9-6" stroke="#e0625a" stroke-width="2" fill="none"/></svg></span><div>EMAIL US<br>hello@brightreed.example</div></div>
  <div class="contact" style="top:262px"><span class="ic"><svg width="16" height="16" viewBox="0 0 24 24"><path d="M12 2a7 7 0 00-7 7c0 5 7 13 7 13s7-8 7-13a7 7 0 00-7-7z" fill="#fff"/><circle cx="12" cy="9" r="2.5" fill="#e0625a"/></svg></span><div>Address line Sample Here<br>Address line Sample</div></div>
  <div class="abs" style="left:0;top:326px;width:1200px;height:1px;background:rgba(255,255,255,.15)"></div>
  <p class="abs" style="left:68px;top:352px;font-size:11px">Copyright © 2025 All Rights Reserved By Bright Reed Studio</p>
  <span class="social" style="left:1016px"></span>
  <span class="social" style="left:1048px"></span>
  <span class="social" style="left:1080px"></span>
  <span class="social" style="left:1112px"></span>
</footer>

</body>
</html>
```